Tech business card design

We need an amazing business card design for our new business 'Brakka' a marketing tech startup based in Sydney, Australia. We provide an online marketplace for businesses to search and buy advertising media, connect with service providers and learn more about marketing. We wish to communicate 'cool tech', reliability and professionalism and design based around our logo.

Target Market(s)

Business Owners

Contact Information for Business Card

Name
Position
Email Address
Website
Phone Number

Font styles to use
Other font styles liked:
• Avenir & Avenir Next

Colors

Designer to choose colors to be used in the design.

```html
<!DOCTYPE html>
<html lang="en">
<head>
<meta charset="utf-8">
<title>Brakka Business Card</title>
<link href="https://fonts.googleapis.com/css2?family=Nunito+Sans:wght@300;400;800&display=swap" rel="stylesheet">
<style>
  :root {
    --backdrop: #2b2d31;
    --card-navy: #1d1b5c;
    --card-navy-deep: #17154b;
    --ink-light: #eceef6;
    --ink-soft: #b9bcd6;
  }
  * { margin: 0; padding: 0; box-sizing: border-box; }
  html, body {
    width: 1200px;
    height: 900px;
    overflow: hidden;
    background: var(--backdrop);
    font-family: "Nunito Sans", sans-serif;
  }
  .card-sheet {
    width: 1200px;
    height: 900px;
    display: flex;
    align-items: center;
    justify-content: center;
    gap: 50px;
  }
  .card {
    position: relative;
    width: 540px;
    height: 320px;
    border-radius: 22px;
    background: linear-gradient(160deg, var(--card-navy) 0%, var(--card-navy-deep) 100%);
    color: var(--ink-light);
  }
  .wordmark {
    font-weight: 800;
    color: var(--ink-light);
    letter-spacing: -1px;
    line-height: 1;
  }
  /* Front */
  .card--front .wordmark {
    position: absolute;
    top: 58px;
    left: 0;
    width: 100%;
    text-align: center;
    font-size: 72px;
  }
  .holder {
    position: absolute;
    top: 150px;
    left: 0;
    width: 100%;
    text-align: center;
  }
  .holder__name {
    font-weight: 800;
    font-size: 19px;
    letter-spacing: 1.5px;
  }
  .holder__role {
    margin-top: 4px;
    font-weight: 300;
    font-size: 12px;
    color: var(--ink-soft);
  }
  .contact {
    position: absolute;
    display: flex;
    align-items: center;
    gap: 8px;
    font-weight: 300;
    font-size: 13px;
    letter-spacing: 2px;
    color: var(--ink-soft);
  }
  .contact svg { width: 11px; height: 11px; flex: none; }
  .contact--phone { left: 40px; bottom: 70px; }
  .contact--email { right: 40px; bottom: 34px; }
  /* Back */
  .card--back .wordmark {
    position: absolute;
    top: 118px;
    left: 0;
    width: 100%;
    text-align: center;
    font-size: 80px;
  }
  .website {
    position: absolute;
    right: 36px;
    bottom: 30px;
    font-weight: 300;
    font-size: 12px;
    letter-spacing: 3px;
    color: var(--ink-soft);
  }
</style>
</head>
<body>
  <main class="card-sheet">
    <section class="card card--front">
      <div class="wordmark">brakka</div>
      <div class="holder">
        <div class="holder__name">Liam Carver</div>
        <div class="holder__role">Founder / Director</div>
      </div>
      <div class="contact contact--phone">
        <svg viewBox="0 0 12 12" aria-hidden="true">
          <rect x="3" y="0.5" width="6" height="11" rx="1" fill="none" stroke="currentColor" stroke-width="1"/>
          <line x1="5" y1="9.5" x2="7" y2="9.5" stroke="currentColor" stroke-width="1"/>
        </svg>
        <span>+61 (0)400 555 201</span>
      </div>
      <div class="contact contact--email">
        <svg viewBox="0 0 12 12" aria-hidden="true">
          <rect x="0.5" y="2" width="11" height="8" rx="1" fill="none" stroke="currentColor" stroke-width="1"/>
          <polyline points="0.8,2.4 6,6.8 11.2,2.4" fill="none" stroke="currentColor" stroke-width="1"/>
        </svg>
        <span>liam@brakkamedia.com.au</span>
      </div>
    </section>

    <section class="card card--back">
      <div class="wordmark">brakka</div>
      <div class="website">www.brakkamedia.com.au</div>
    </section>
  </main>
</body>
</html>
```